Company Website Re-design for Software development consultancy

We would like our company website to be redesigned using our existing marketing collateral and website content as a guide

current site : www.brackenloft.com.au

For the different pages types and content please base on the following site : https://www.quorvanta.net/

We want a coded site - but will replace the content ourselves within the sections you provide to customise to our needs.

Target Market(s)

Medium to Large corporates needing software design and development services

Industry/Entity Type

Information Technology

Coding

Coded - Design and coding required

Number of Pages Required

5+ page

Font styles to use
Sans Serif

Colors
ec1f27
ffffff
000000

Requirements
Must have
• Align to colour scheme of existing collateral
• Include pages for the key areas of our busines - see : https://www.quorvanta.net/
Nice to have
• image rotators - make the site interesting to the business visitor

```html
<!DOCTYPE html>
<html lang="en">
<head>
<meta charset="utf-8">
<title>Bracken Loft – Software Development Services</title>
<link href="https://fonts.googleapis.com/css2?family=Roboto+Condensed:wght@400;700&family=Open+Sans:ital,wght@0,400;0,600;0,700;1,400;1,600&display=swap" rel="stylesheet">
<style>
:root{
  --red:#ec1f27;
  --white:#ffffff;
  --black:#000000;
  --ink:#222222;
  --text:#666666;
  --muted:#9a9a9a;
  --line:#e3e3e3;
  --grey-bg:#eeeeee;
  --dark:#3a3a3a;
  --darker:#2e2e2e;
  --deepest:#1f1f1f;
  --head:"Roboto Condensed",Arial,sans-serif;
  --body:"Open Sans",Arial,sans-serif;
}
*{margin:0;padding:0;box-sizing:border-box}
html,body{width:1200px;height:4082px;overflow:hidden}
body{font-family:var(--body);color:var(--text);background:var(--white);position:relative}
section,header,footer{position:relative;width:1200px}
.abs{position:absolute}
h1,h2,h3,h4{font-family:var(--head);color:var(--ink)}
.sq{display:inline-block;width:14px;height:14px;border-radius:2px}

/* top bar */
.topbar{height:27px;border-bottom:1px solid var(--line);font-size:10px;color:#555}
.topbar .abs{top:8px;display:flex;align-items:center;gap:6px}
.topbar .social .sq{background:#555}

/* nav */
.nav{height:68px}
.logo{font-family:var(--head);font-weight:700;font-size:30px;letter-spacing:1px;color:var(--black)}
.nav .logo{left:158px;top:16px}
.menu{right:220px;top:26px;display:flex;gap:38px;font-size:11px;font-weight:600;color:#444}
.menu .active{color:var(--red)}
.cta{right:52px;top:15px;background:var(--red);color:#fff;font-size:11px;font-weight:700;padding:9px 20px;border-radius:20px}

/* hero */
.hero{height:525px;background:linear-gradient(100deg,#4a535c 0%,#7d8790 38%,#c9cfd4 70%,#dfe3e6 100%)}
.hero-copy{left:503px;top:168px;color:#fff}
.hero-copy h3{color:#fff;font-size:27px;font-weight:700}
.hero-copy h1{color:#fff;font-size:54px;font-weight:700;line-height:1;margin-top:2px}
.hero-copy p{font-size:13px;width:560px;margin-top:8px;line-height:1.5}
.btn{display:inline-flex;align-items:center;gap:10px;font-size:10px;font-weight:700;padding:9px 20px;border-radius:18px;color:#fff;background:var(--dark)}
.btn.red{background:var(--red)}
.btn.light{background:#eee;color:#333}
.hero .btn{position:absolute;left:503px;top:412px}

/* faces */
.faces{height:510px}
.faces .eyebrow{left:158px;top:78px;color:var(--red);font-family:var(--head);font-weight:700;font-size:24px}
.faces h2{position:absolute;left:158px;top:102px;font-size:42px}
.faces .tag{left:158px;top:153px;font-size:10px;font-weight:700;letter-spacing:2px;color:#444}
.faces .intro{left:590px;top:96px;width:450px;font-size:10.5px;line-height:1.7}
.face{top:205px;width:272px}
.face .num{font-family:var(--head);font-weight:700;font-size:110px;color:#f0f0f0;line-height:1}
.face h4{position:absolute;left:88px;top:80px;font-size:20px;letter-spacing:.5px;display:flex;align-items:center;gap:12px}
.face h4:after{content:"";width:28px;height:2px;background:#555}
.face svg{position:absolute;right:0;top:12px}
.face p{font-size:10.5px;line-height:1.65;margin-top:8px}
.face .btn{margin-top:22px}

/* offer */
.offer{height:590px;background:linear-gradient(180deg,#f1f1f1,#e4e4e4)}
.center{text-align:center;width:100%;left:0}
.sec-title{font-size:38px;font-weight:700}
.sec-sub{font-size:10px;font-weight:700;letter-spacing:1.5px;color:#444;margin-top:2px}
.sec-text{font-size:10.5px;line-height:1.7;width:900px;margin:12px auto 0}
.offer .head{top:60px}
.cards{left:38px;top:195px;display:flex;gap:11px}
.card{width:218px;height:327px;background:#fff;text-align:center;padding-top:35px;box-shadow:0 2px 6px rgba(0,0,0,.08)}
.card .ico{width:88px;height:88px;border-radius:50%;background:#444;margin:0 auto;display:flex;align-items:center;justify-content:center;border:6px solid #ddd}
.card.hot .ico{background:var(--red);border-color:#f7b8bb}
.card h4{font-size:17px;margin-top:22px}
.card p{font-size:10.5px;line-height:1.6;padding:8px 22px 0}
.card .btn{margin-top:16px}

/* goal */
.goal{height:416px;background:linear-gradient(180deg,#3f3f3f,#2f2f2f)}
.goal h2{position:absolute;left:158px;top:70px;color:#fff;font-size:40px}
.goal .sub{left:158px;top:116px;color:#ddd;font-size:10px;font-weight:700;letter-spacing:1.5px}
.goal .intro{left:558px;top:62px;width:500px;font-size:10.5px;line-height:1.7;color:#aaa}
.stat{top:150px;width:190px;height:190px;border-radius:50%;background:#555;display:flex;align-items:center;justify-content:center}
.stat .inner{width:160px;height:160px;border-radius:50%;background:#e9e9e9;border:2px dashed #aaa;display:flex;flex-direction:column;align-items:center;justify-content:center}
.stat b{font-family:var(--head);font-size:40px;color:var(--ink)}
.stat span{font-size:10px;font-weight:700;color:#444}

/* work */
.work{height:585px}
.work .head{top:62px}
.filters{top:220px;display:flex;justify-content:center;gap:26px;font-size:11px;font-weight:600;color:#444}
.filters .on{background:var(--red);color:#fff;padding:5px 14px;border-radius:14px;margin-top:-5px}
.tiles{left:38px;top:256px;display:flex}
.tile{width:224.8px;height:206px}
.t1{background:linear-gradient(135deg,#f4f1e8,#d9e4cf)}
.t2{background:linear-gradient(135deg,#e7e7e7,#bdbdbd)}
.t3{background:var(--red);color:#fff;text-align:center;display:flex;flex-direction:column;align-items:center;justify-content:center}
.t3 b{font-family:var(--head);font-size:22px}
.t3 small{font-size:9px;font-weight:700;letter-spacing:1px}
.t4{background:linear-gradient(135deg,#7fc8e8,#3c8fc4)}
.t5{background:linear-gradient(135deg,#5f6e7c,#8a98a6)}
.dots{top:504px;display:flex;justify-content:center;gap:6px}
.dots i{width:9px;height:9px;border-radius:50%;background:#ccc}
.dots i:first-child{background:#888}

/* testimonial */
.says{height:250px;background:#3c3c3c}
.says h2{position:absolute;left:158px;top:100px;color:#fff;font-size:40px}
.says .sub{left:158px;top:146px;color:#ddd;font-size:10px;font-weight:700;letter-spacing:1.5px}
.quote{left:498px;top:0;width:702px;height:250px;background:#2b2b2b}
.quote p{position:absolute;left:42px;top:68px;width:560px;color:#eee;font-style:italic;font-size:14px;line-height:1.55;font-weight:600}
.quote .who{position:absolute;left:42px;top:170px;display:flex;align-items:center;gap:10px;color:#ddd;font-size:12px}
.quote .who i{width:30px;height:30px;border-radius:50%;background:#7a6a60}

/* clients */
.clients{height:117px;border-bottom:1px solid var(--line)}
.client-row{top:40px;left:150px;width:900px;display:flex;justify-content:space-between;align-items:center;font-family:var(--head);font-size:24px;font-weight:700;color:#888}

/* team */
.team{height:599px}
.team .head{top:66px}
.member{top:212px;width:190px;text-align:center}
.member .photo{height:243px;background:linear-gradient(180deg,#f4f4f4,#c9ccd0)}
.member h4{font-size:17px;margin-top:32px;letter-spacing:.5px}
.member .social{margin-top:8px;display:flex;justify-content:center;gap:6px}
.member .social .sq{background:#555}

/* footer */
.footer{height:346px;background:linear-gradient(180deg,#3d3d3d,#333)}
.footer .logo{position:absolute;color:#fff;top:50px;width:100%;text-align:center}
.contact{top:115px;width:240px;text-align:center;color:#eee;font-size:11px}
.contact svg{display:block;margin:0 auto 8px}
.footer h3{position:absolute;top:210px;width:100%;text-align:center;color:#fff;font-size:20px;letter-spacing:1px}
.sub-form{left:345px;top:258px;display:flex}
.sub-form span{width:371px;height:44px;background:#fff;border-radius:22px 0 0 22px;font-size:10px;color:#999;padding:15px 22px}
.sub-form b{width:139px;height:44px;background:var(--red);color:#fff;border-radius:22px;margin-left:-20px;font-size:12px;text-align:center;line-height:44px}
.bottom{height:49px;background:var(--deepest);font-size:9.5px;color:#ccc}
.bottom .links{left:158px;top:18px;display:flex;gap:26px}
.bottom .copy{right:130px;top:18px}
</style>
</head>
<body>

<header class="topbar">
  <div class="abs" style="left:158px">Address : 42 Harlow Lane, Sydney 2000</div>
  <div class="abs" style="left:470px">Email : info@brackenloft.com.au</div>
  <div class="abs" style="left:725px">Call us : 555-014-2290</div>
  <div class="abs social" style="left:958px"><i class="sq"></i><i class="sq"></i><i class="sq"></i><i class="sq"></i><i class="sq"></i></div>
</header>

<header class="nav">
  <div class="abs logo">BRACKEN LOFT</div>
  <nav class="abs menu"><span class="active">HOME</span><span>ABOUT US</span><span>OUR SERVICES</span><span>PROJECT</span><span>OUR TEAM</span></nav>
  <div class="abs cta">GET IN TOUCH</div>
</header>

<section class="hero" role="img" aria-label="Photo of a developer working at a computer in a bright office">
  <div class="abs hero-copy">
    <h3>PROFESSIONAL SOFTWARE</h3>
    <h1>DEVELOPMENT SERVICES</h1>
    <p>Lorem ipsum dolor sit amet, consectetur adipiscing elit. Sed ligula nisi, suscipit non lorem eget fine tincidunt laoreet, ipsum at tincidunt augue quisque.</p>
  </div>
  <span class="btn light">CLICK HERE &rarr;</span>
</section>

<section class="faces">
  <div class="abs eyebrow">THE THREE FACES</div>
  <h2>OF BRACKEN LOFT</h2>
  <div class="abs tag">WE ARE ALL ABOUT BUILDING SOFTWARE BETTER.</div>
  <p class="abs intro">Quisque sapien quam, viverra eleifend est eu, varius dapibus tortor. Quisque ac pulvinar velit. Integer et ipsum at velit vehicula Lorem ipsum dolor sit amet, consectetur adipiscing elit. Sed ligula nisi, suscipit non tortor eget, fringilla tincidunt dolor Lorem ipsum dolor sit amet, consectetur adipiscing elit. Sed ligula nisi, suscipit non.</p>

  <div class="abs face" style="left:158px">
    <div class="num">01</div>
    <h4>CONSULTING</h4>
    <svg width="34" height="34" viewBox="0 0 34 34"><circle cx="14" cy="10" r="7" fill="#ec1f27"/><path d="M2 32c0-8 6-13 12-13s12 5 12 13z" fill="#ec1f27"/><circle cx="27" cy="24" r="6" fill="#fff" stroke="#ec1f27" stroke-width="2"/></svg>
    <p>Lorem ipsum dolor sit amet, consectetur adipiscing elit. Sed ligula nisi, suscipit non tortor eget, fringilla tincidunt dolor Lorem ipsum dolor sit amet.</p>
    <span class="btn red">LEARN MORE &rarr;</span>
  </div>
  <div class="abs face" style="left:465px">
    <div class="num">02</div>
    <h4>PROJECTS</h4>
    <svg width="34" height="34" viewBox="0 0 34 34" fill="none" stroke="#333" stroke-width="2"><rect x="6" y="5" width="20" height="26" rx="2"/><path d="M11 12h10M11 18h10M11 24h6"/><circle cx="25" cy="25" r="5" fill="#fff"/></svg>
    <p>Lorem ipsum dolor sit amet, consectetur adipiscing elit. Sed ligula nisi, suscipit non tortor eget, fringilla tincidunt dolor Lorem ipsum dolor sit amet.</p>
    <span class="btn">LEARN MORE &rarr;</span>
  </div>
  <div class="abs face" style="left:773px">
    <div class="num">03</div>
    <h4>IMPRESS</h4>
    <svg width="34" height="34" viewBox="0 0 34 34" fill="none" stroke="#333" stroke-width="2"><path d="M8 4h13l6 6v20H8z"/><path d="M12 16h11M12 21h11M12 26h7"/></svg>
    <p>Lorem ipsum dolor sit amet, consectetur adipiscing elit. Sed ligula nisi, suscipit non tortor eget, fringilla tincidunt dolor Lorem ipsum dolor sit amet.</p>
    <span class="btn">LEARN MORE &rarr;</span>
  </div>
</section>

<section class="offer">
  <div class="abs center head">
    <h2 class="sec-title">WHAT WE OFFER</h2>
    <div class="sec-sub">OUR AWSOME SERVICES</div>
    <p class="sec-text">Quisque sapien quam, viverra eleifend est eu, varius dapibus tortor. Quisque ac pulvinar velit. Integer et ipsum at velit vehicula Lorem ipsum dolor sit amet, consectetur adipiscing elit. Sed ligula nisi, suscipit non tortor eget, fringilla tincidunt dolor Lorem ipsum dolor sit amet, suscipit non.</p>
  </div>
  <div class="abs cards">
    <div class="card hot">
      <div class="ico"><svg width="36" height="30" viewBox="0 0 36 30" fill="none" stroke="#fff" stroke-width="2"><rect x="2" y="2" width="32" height="20" rx="2"/><path d="M12 28h12M18 22v6"/></svg></div>
      <h4>ERP SOLUTIONS</h4>
      <p>Fusce cursus ante lectus, in cursus dui suscipit quis. Phasellus at placerat magna. Nulla diam nunc, tincidunt vel bibendum quis, molestie in risus.</p>
      <span class="btn red">VIEW DETAILS &rarr;</span>
    </div>
    <div class="card">
      <div class="ico"><svg width="36" height="30" viewBox="0 0 36 30" fill="none" stroke="#fff" stroke-width="2"><rect x="2" y="2" width="32" height="20" rx="2"/><circle cx="18" cy="12" r="5"/><path d="M12 28h12"/></svg></div>
      <h4>SOFTWARE SOLUTIONS</h4>
      <p>Fusce cursus ante lectus, in cursus dui suscipit quis. Phasellus at placerat magna. Nulla diam nunc, tincidunt vel bibendum quis, molestie in risus.</p>
      <span class="btn">VIEW DETAILS &rarr;</span>
    </div>
    <div class="card">
      <div class="ico"><svg width="36" height="30" viewBox="0 0 36 30" fill="none" stroke="#fff" stroke-width="2"><rect x="2" y="2" width="32" height="20" rx="2"/><path d="M14 8l-4 4 4 4M22 8l4 4-4 4M12 28h12"/></svg></div>
      <h4>DIGITAL MAKETING</h4>
      <p>Fusce cursus ante lectus, in cursus dui suscipit quis. Phasellus at placerat magna. Nulla diam nunc, tincidunt vel bibendum quis, molestie in risus.</p>
      <span class="btn">VIEW DETAILS &rarr;</span>
    </div>
    <div class="card">
      <div class="ico"><svg width="24" height="34" viewBox="0 0 24 34" fill="none" stroke="#fff" stroke-width="2"><rect x="2" y="2" width="20" height="30" rx="3"/><path d="M9 27h6"/></svg></div>
      <h4>MOBILE APP</h4>
      <p>Fusce cursus ante lectus, in cursus dui suscipit quis. Phasellus at placerat magna. Nulla diam nunc, tincidunt vel bibendum quis, molestie in risus.</p>
      <span class="btn">VIEW DETAILS &rarr;</span>
    </div>
    <div class="card">
      <div class="ico"><svg width="38" height="28" viewBox="0 0 38 28" fill="none" stroke="#fff" stroke-width="2"><path d="M10 24a7 7 0 0 1 0-14 10 10 0 0 1 19 2 6 6 0 0 1 0 12z"/></svg></div>
      <h4>CLOUD SERVICE</h4>
      <p>Fusce cursus ante lectus, in cursus dui suscipit quis. Phasellus at placerat magna. Nulla diam nunc, tincidunt vel bibendum quis, molestie in risus.</p>
      <span class="btn">VIEW DETAILS &rarr;</span>
    </div>
  </div>
</section>

<section class="goal">
  <h2>OUR GOAL</h2>
  <div class="abs sub">TRACK RECORDS</div>
  <p class="abs intro">Quisque sapien quam, viverra eleifend est eu, varius dapibus tortor. Quisque ac pulvinar velit. Integer et ipsum at velit vehicula Lorem ipsum dolor sit amet, consectetur adipiscing elit. Sed ligula nisi, suscipit non tortor eget, fringilla tincidunt dolor sit amet.</p>
  <div class="abs stat" style="left:166px"><div class="inner"><b>30+</b><span>YEARS OF EXPERIENCE</span></div></div>
  <div class="abs stat" style="left:389px"><div class="inner"><b>250+</b><span>TEAM SIZE</span></div></div>
  <div class="abs stat" style="left:612px"><div class="inner"><b>2500+</b><span>CLIENTS</span></div></div>
  <div class="abs stat" style="left:838px"><div class="inner"><b>3500+</b><span>PROJECTS</span></div></div>
</section>

<section class="work">
  <div class="abs center head">
    <h2 class="sec-title">RECENT WORK</h2>
    <div class="sec-sub">OUR AWSOME PORTFOLIO</div>
    <p class="sec-text">Quisque sapien quam, viverra eleifend est eu, varius dapibus tortor. Quisque ac pulvinar velit. Integer et ipsum at velit vehicula Lorem ipsum dolor sit amet, consectetur adipiscing elit. Sed ligula nisi, suscipit non tortor eget, fringilla tincidunt dolor Lorem ipsum dolor sit amet.</p>
  </div>
  <div class="abs center filters"><span class="on">ALL</span><span>WEB DESIGN</span><span>LOGO DESIGN</span><span>MOBILE APPS</span></div>
  <div class="abs tiles">
    <div class="tile t1" role="img" aria-label="Portfolio shot of printed brochure designs"></div>
    <div class="tile t2" role="img" aria-label="Portfolio shot of a desk with a lamp and laptop"></div>
    <div class="tile t3"><svg width="30" height="30" viewBox="0 0 30 30" stroke="#fff" stroke-width="2"><path d="M15 2v26M2 15h26"/></svg><b>WEB DESIGN</b><small>WEB DESIGN PORTFOLIO</small></div>
    <div class="tile t4" role="img" aria-label="Portfolio shot of a website shown on a monitor"></div>
    <div class="tile t5" role="img" aria-label="Portfolio shot of stationery and a calculator on a desk"></div>
  </div>
  <div class="abs center dots"><i></i><i></i><i></i><i></i></div>
</section>

<section class="says">
  <h2>OUR CLIENT SAYS</h2>
  <div class="abs sub">TESTIMONIALS</div>
  <div class="abs quote">
    <p>Fusce cursus ante lectus, in cursus dui suscipit quis. Phasellus at placerat magna. Nulla diam nunc, tincidunt vel bibendum quis, molestie in risus. Fusce at ipsum faucibus, facilisis turpis nec, interdum lacus. Suspendisse a venenatis lectus, non sollicitudin orci. Aenean facilisis vestibulum</p>
    <div class="who"><i role="img" aria-label="Client portrait"></i>Marcus Deane (Canada)</div>
  </div>
</section>

<section class="clients">
  <div class="abs client-row"><span>Veltrix</span><span>Norvale</span><span>Alder College</span><span>Kestwick</span><span>Solmara</span><span>Brightpath</span></div>
</section>

<section class="team">
  <div class="abs center head">
    <h2 class="sec-title">OUR LEADERSHIP TEAM</h2>
    <div class="sec-sub">OUR EXPERTISE</div>
    <p class="sec-text">Quisque sapien quam, viverra eleifend est eu, varius dapibus tortor. Quisque ac pulvinar velit. Integer et ipsum at velit vehicula Lorem ipsum dolor sit amet, consectetur adipiscing elit. Sed ligula nisi, suscipit non tortor eget, fringilla tincidunt dolor sit amet.</p>
  </div>
  <div class="abs member" style="left:207px"><div class="photo" role="img" aria-label="Portrait of a team leader in business attire"></div><h4>ELENA VARGA</h4><div class="social"><i class="sq"></i><i class="sq"></i><i class="sq"></i></div></div>
  <div class="abs member" style="left:504px"><div class="photo" role="img" aria-label="Portrait of a team leader in a suit"></div><h4>GRAHAM WHITCOMBE</h4><div class="social"><i class="sq"></i><i class="sq"></i><i class="sq"></i></div></div>
  <div class="abs member" style="left:803px"><div class="photo" role="img" aria-label="Portrait of a team leader in a suit"></div><h4>OWEN CALDER</h4><div class="social"><i class="sq"></i><i class="sq"></i><i class="sq"></i></div></div>
</section>

<footer class="footer">
  <div class="logo">BRACKEN LOFT</div>
  <div class="abs contact" style="left:182px"><svg width="20" height="20" viewBox="0 0 24 24" fill="#fff"><path d="M6.6 10.8a15 15 0 0 0 6.6 6.6l2.2-2.2c.3-.3.7-.4 1-.2 1.1.4 2.3.6 3.6.6.6 0 1 .4 1 1V20c0 .6-.4 1-1 1A17 17 0 0 1 3 4c0-.6.4-1 1-1h3.5c.6 0 1 .4 1 1 0 1.3.2 2.5.6 3.6.1.3 0 .7-.2 1z"/></svg>555-014-2290</div>
  <div class="abs contact" style="left:479px"><svg width="22" height="20" viewBox="0 0 24 20" fill="none" stroke="#fff" stroke-width="2"><rect x="2" y="3" width="20" height="14"/><path d="M2 3l10 8 10-8"/></svg>INFO@BRACKENLOFT.COM.AU</div>
  <div class="abs contact" style="left:778px"><svg width="18" height="22" viewBox="0 0 18 24" fill="#fff"><path d="M9 0a9 9 0 0 0-9 9c0 7 9 15 9 15s9-8 9-15a9 9 0 0 0-9-9zm0 12a3 3 0 1 1 0-6 3 3 0 0 1 0 6z"/></svg>42 HARLOW LANE, SYDNEY 2000</div>
  <h3>SUBSCRIBE OUR NEWSLETTER</h3>
  <div class="abs sub-form"><span>ENTER YOUR EMAIL ID</span><b>SUBSCRIBE</b></div>
</footer>

<footer class="bottom">
  <div class="abs links"><span>HOME</span><span>ABOUT US</span><span>OUR SERVICES</span><span>PROJECT</span><span>OUR TEAM</span><span>CONTACT US</span></div>
  <div class="abs copy">COPYRIGHT 2018. ALL RIGHT RESERVED</div>
</footer>

</body>
</html>
```